new letterhead for my brokergae company BoatCrest, Complete Marine Brokering

We need a new letterhead for our brokerage company called BoatCrest. We are specialised in selling pleasure crafts (sailing and motoryachts). More info can be found at https://boatcrest-example.com/en

I use this document for a quotation, a letter, sales agreement, selling instructions. I am looking for a cover page + a content page.

Th efollowing information needs to be in the header / footer; email, website, VAT number, Bank Account number, number chamber of ccomerce, registry number orvd, General terms and conditions KLTV apply.

```html
<!DOCTYPE html>
<html lang="en">
<head>
<meta charset="utf-8">
<title>BoatCrest Letterhead</title>
<link href="https://fonts.googleapis.com/css2?family=Open+Sans:wght@400;600;700&display=swap" rel="stylesheet">
<style>
  :root {
    --backdrop: #e9edf6;
    --paper: #f6f6f5;
    --brand-blue: #1c5aa6;
    --ink: #3d4450;
    --band-text: #ffffff;
  }
  * { box-sizing: border-box; margin: 0; padding: 0; }
  html, body {
    width: 1200px; height: 900px; overflow: hidden;
    background: var(--backdrop);
    font-family: "Open Sans", Arial, sans-serif;
  }
  .letterhead {
    position: absolute; left: 300px; top: 26px;
    width: 600px; height: 848px;
    background: var(--paper);
    box-shadow: 0 4px 18px rgba(40, 60, 100, 0.15);
  }
  .brand {
    position: absolute; left: 46px; top: 42px;
    color: var(--brand-blue);
  }
  .brand-name {
    display: flex; align-items: center; gap: 8px;
    font-size: 28px; font-weight: 600; line-height: 1;
  }
  .brand-dot {
    width: 14px; height: 14px; border-radius: 50%;
    background: var(--brand-blue);
  }
  .brand-tagline {
    margin-top: 6px; margin-left: 22px;
    font-size: 7.5px; font-weight: 700; letter-spacing: 1.6px;
    text-transform: uppercase;
  }
  .contact {
    position: absolute; left: 458px; top: 64px;
    border-left: 2.5px solid var(--brand-blue);
    padding-left: 8px;
    font-size: 8.5px; color: var(--ink); line-height: 11.5px;
  }
  .contact-row { display: flex; align-items: center; gap: 5px; }
  .contact-row svg { width: 7px; height: 7px; flex: none; }
  .terms-band {
    position: absolute; left: 0; top: 770px;
    width: 600px; height: 52px;
    background: var(--brand-blue);
    color: var(--band-text);
    font-size: 7px; line-height: 10px; text-align: center;
    padding: 8px 70px 0 14px;
  }
  .registry-line {
    position: absolute; left: 0; top: 826px; width: 530px;
    text-align: center; font-size: 7px; color: var(--ink);
  }
</style>
</head>
<body>
  <main class="letterhead">
    <header>
      <div class="brand">
        <div class="brand-name"><span class="brand-dot"></span>BoatCrest</div>
        <div class="brand-tagline">Complete Marine Brokering</div>
      </div>
      <div class="contact">
        <div class="contact-row">
          <svg viewBox="0 0 10 10"><path d="M2 1 L4 1 L4.6 3.2 L3.4 4 Q4.4 6 6 6.6 L6.8 5.4 L9 6 L9 8 Q5 9.5 1 5 Q1 3 2 1 Z" fill="var(--brand-blue)"/></svg>
          +31 20 555 01 42
        </div>
        <div class="contact-row">
          <svg viewBox="0 0 10 10"><rect x="0.8" y="2" width="8.4" height="6" fill="none" stroke="var(--brand-blue)" stroke-width="1.2"/><path d="M1 2.3 L5 5.5 L9 2.3" fill="none" stroke="var(--brand-blue)" stroke-width="1.1"/></svg>
          info@boatcrest-example.com
        </div>
        <div class="contact-row">
          <svg viewBox="0 0 10 10"><circle cx="5" cy="5" r="4" fill="none" stroke="var(--brand-blue)" stroke-width="1.1"/><ellipse cx="5" cy="5" rx="1.8" ry="4" fill="none" stroke="var(--brand-blue)" stroke-width="0.9"/><path d="M1 5 H9" stroke="var(--brand-blue)" stroke-width="0.9"/></svg>
          www.boatcrest-example.com
        </div>
      </div>
    </header>

    <footer>
      <p class="terms-band">These general terms and conditions have been laid down by the 'Coastal League of Vessel Traders' (Kustliga van Taxateurs en Verkopers, KLTV) and filed at the court registry of the court in Amsterdam on 13/04/2017 under number 28/2017 in Dutch. These terms and conditions apply exclusively to members of the KLTV. The terms and conditions came into force on 15/05/2017. ©Coastal League of Vessel Traders.</p>
      <p class="registry-line">VAT # 0000000 &nbsp;|&nbsp; Bank Account #: 0000 0000 0000 0000 &nbsp;|&nbsp; # Chamber of Commerce &nbsp;|&nbsp; Registry Number ORVD</p>
    </footer>
  </main>
</body>
</html>
```